BrivoPeak Business Card Design Project

We are looking for a modern, clean business card design for our new company. We are a consulting firm focused on the financial services market providing management and IT consulting to banks, insurance companies, etc. Please include our company logo and company contact information from the attached file in the design. Two versions of the logo are attached, either version is acceptable. Logos are available in other file formats if needed. We would like to include the contact information for both our UK and US offices as well as the following information for each individual card holder: Name, position/title, address, phone number and e-mail address.
Updates
Project Deadline Extended
Reason: A last minute trip over seas has prevented us from finalizing the decision. A decision will be made this week. We apologize for the inconvenience.
Industry/Entity Type
Business
Contact Information for Business Card
Company logo.
Company locations and phone numbers for both the US and UK offices.
Company URL.
Cardholder Name
Cardholder Position/title
Cardholder Address
Cardholder Phone Number
Cardholder e-mail Address
Look and feel
Each slider illustrates characteristics of the customer's brand and the style your logo design should communicate.

```html
<!DOCTYPE html>
<html lang="en">
<head>
<meta charset="utf-8">
<title>BrivoPeak Partners – Business Card</title>
<link href="https://fonts.googleapis.com/css2?family=Roboto:wght@400;700&display=swap" rel="stylesheet">
<style>
  :root {
    --page-bg: #e9e6e1;
    --card-dark: #0b0b0b;
    --card-light: #f6f6f6;
    --band-grey: #8a8a8a;
    --brand-blue: #2f5593;
    --band-blue: #1f3f78;
    --text-grey: #5a5a5a;
    --rule-grey: #b9b9b9;
    --white: #ffffff;
  }
  * { margin: 0; padding: 0; box-sizing: border-box; }
  html, body {
    width: 1200px; height: 902px; overflow: hidden;
    background: var(--page-bg);
    font-family: "Roboto", Arial, sans-serif;
  }
  .canvas { position: relative; width: 1200px; height: 902px; }
  .card {
    position: absolute; width: 620px; height: 354px;
    left: 290px; overflow: hidden;
    box-shadow: 0 6px 18px rgba(0,0,0,.18);
  }
  .card--back { top: 62px; background: var(--card-dark); }
  .card--front { top: 486px; background: var(--card-light); }

  .band { position: absolute; left: 0; right: 0; bottom: 0; height: 44px; }
  .card--back .band { background: var(--band-grey); }
  .card--front .band { background: var(--band-blue); }

  .brand-name {
    font-weight: 700; text-align: center; line-height: 1;
  }
  .brand-name .line-main { display: block; font-size: 58px; letter-spacing: -0.5px; }
  .brand-name .line-sub { display: block; font-size: 22px; letter-spacing: 4px; margin-top: 8px; }

  .card--back .brand-name {
    position: absolute; top: 64px; left: 0; right: 0; color: var(--white);
  }
  .addresses {
    position: absolute; top: 210px; left: 0; right: 0;
    text-align: center; color: var(--white); font-size: 15px; line-height: 1.55;
  }

  .card--front .brand-name {
    position: absolute; top: 118px; left: 28px; width: 300px; color: var(--brand-blue);
  }
  .card--front .brand-name .line-main { font-size: 48px; }
  .card--front .brand-name .line-sub { font-size: 19px; }
  .divider {
    position: absolute; left: 342px; top: 40px; width: 1px; height: 230px;
    background: var(--rule-grey);
  }
  .holder { position: absolute; left: 368px; top: 50px; }
  .holder-name { color: var(--brand-blue); font-size: 28px; font-weight: 400; line-height: 1.1; }
  .holder-title { color: var(--text-grey); font-size: 17px; margin-top: 2px; }
  .contacts { list-style: none; margin-top: 26px; color: var(--text-grey); font-size: 14px; }
  .contacts li { display: flex; align-items: center; gap: 9px; height: 24px; }
  .contacts svg { width: 14px; height: 14px; flex: none; }
</style>
</head>
<body>
<main class="canvas">

  <section class="card card--back" aria-label="Business card back">
    <h1 class="brand-name">
      <span class="line-main">BrivoPeak</span>
      <span class="line-sub">PARTNERS</span>
    </h1>
    <address class="addresses">
      14 Harlow Street, London, E2 8QP, Great Britain<br>
      780 N Cedar Ave, Suite 204-210, Lakeford UT 84120, United States
    </address>
    <div class="band"></div>
  </section>

  <section class="card card--front" aria-label="Business card front">
    <h2 class="brand-name">
      <span class="line-main">BrivoPeak</span>
      <span class="line-sub">PARTNERS</span>
    </h2>
    <div class="divider"></div>
    <div class="holder">
      <p class="holder-name">Elian Marsh</p>
      <p class="holder-title">Managing Director</p>
      <ul class="contacts">
        <li>
          <svg viewBox="0 0 14 14"><rect width="14" height="14" rx="2" fill="var(--brand-blue)"/><path d="M4 3.5h2l.7 2-1.2.8a5 5 0 0 0 2.2 2.2l.8-1.2 2 .7v2c0 .5-.4.8-.9.8A6.6 6.6 0 0 1 3.2 4.4c0-.5.3-.9.8-.9z" fill="#fff"/></svg>
          US: (801) 555-0142
        </li>
        <li>
          <svg viewBox="0 0 14 14"><rect width="14" height="14" rx="2" fill="var(--brand-blue)"/><path d="M4 3.5h2l.7 2-1.2.8a5 5 0 0 0 2.2 2.2l.8-1.2 2 .7v2c0 .5-.4.8-.9.8A6.6 6.6 0 0 1 3.2 4.4c0-.5.3-.9.8-.9z" fill="#fff"/></svg>
          UK: +44 7700 900418
        </li>
        <li>
          <svg viewBox="0 0 14 14"><rect width="14" height="14" rx="2" fill="var(--brand-blue)"/><rect x="3" y="4.5" width="8" height="5.5" fill="none" stroke="#fff" stroke-width="1"/><path d="M3 4.5l4 3 4-3" fill="none" stroke="#fff" stroke-width="1"/></svg>
          elian@brivopeakpartners.com
        </li>
        <li>
          <svg viewBox="0 0 14 14"><rect width="14" height="14" rx="2" fill="var(--brand-blue)"/><circle cx="7" cy="7" r="3.6" fill="none" stroke="#fff" stroke-width="1"/><path d="M3.4 7h7.2M7 3.4c-1.6 2-1.6 5.2 0 7.2M7 3.4c1.6 2 1.6 5.2 0 7.2" fill="none" stroke="#fff" stroke-width=".8"/></svg>
          www.brivopeakpartners.com
        </li>
      </ul>
    </div>
    <div class="band"></div>
  </section>

</main>
</body>
</html>
```